Wine Label Design for Marrick Estate

I need a front and back label for a new wine I am making. I am looking for a classic, elegant and serious wine label. I would like the label to be white with blue and black writing. The blue will be the distinction in the label. The color of blue will be unique and catch the eye. The font of the writing will be unique and could also serve as the brand image for Marrick Estate. The label can have a design but should be simple and distinct. I envision the paper quality of the label to textured, high quality and add to the overall image of the label.
The label will be timeless. The price of this wine will be $85.00 a bottle, and the label should match a higher priced wine. This wine is family owned and operated.
The writing on the front and back label will be:

FRONT Label-

Marrick Estate

Howell Mountain

Napa Valley

2022 Cabernet Sauvignon

Back Label-

Cellared and Bottled by Marrick Estate, Calder Ridge, CA 95417

GOVERNMENT WARNING: (1) According to the Surgeon General, women should not drink alcoholic beverages during pregnancy because of the risk of birth defects. (2) Consumption of alcoholic beverages impairs your ability to drive a car or operate machinery, and may cause health problems.

Alc. 14.5% by Vol.

750 ml

Contains Sulfites

```html
<!DOCTYPE html>
<html lang="en">
<head>
<meta charset="UTF-8">
<title>Marrick Estate – Front and Back Label</title>
<link href="https://fonts.googleapis.com/css2?family=Bodoni+Moda:wght@500&family=Josefin+Sans:wght@400;600&family=Pinyon+Script&display=swap" rel="stylesheet">
<style>
  :root {
    --backdrop: #3b3c40;
    --paper: #f4f5f7;
    --paper-shade: #e3e5ea;
    --estate-blue: #2a2fa3;
    --ink: #222226;
    --frame: #3a3a40;
  }
  * { box-sizing: border-box; margin: 0; padding: 0; }
  html, body { width: 1200px; height: 900px; overflow: hidden; }
  body {
    background: var(--backdrop);
    font-family: "Josefin Sans", sans-serif;
    color: var(--ink);
    position: relative;
  }
  .label {
    position: absolute;
    top: 190px;
    width: 420px;
    height: 620px;
    background: radial-gradient(ellipse at 60% 35%, var(--paper) 0%, var(--paper) 55%, var(--paper-shade) 100%);
    text-align: center;
  }
  .label--front { left: 150px; }
  .label--back { left: 630px; }
  .label__frame {
    position: absolute;
    inset: 14px;
    border: 1.5px solid var(--frame);
  }
  .seal {
    position: absolute;
    left: 50%;
    top: -70px;
    width: 150px;
    height: 150px;
    margin-left: -75px;
    border-radius: 50%;
    background: var(--paper);
    display: flex;
    align-items: center;
    justify-content: center;
  }
  .seal__ring {
    width: 118px;
    height: 118px;
    border-radius: 50%;
    border: 3px solid var(--estate-blue);
    display: flex;
    align-items: center;
    justify-content: center;
    font-family: "Bodoni Moda", serif;
    font-size: 15px;
    letter-spacing: 2px;
    color: var(--estate-blue);
  }
  .brand {
    font-family: "Bodoni Moda", serif;
    font-weight: 500;
    color: var(--estate-blue);
    line-height: 1;
  }
  .brand__name { display: block; letter-spacing: 9px; padding-left: 9px; }
  .brand__estate { display: block; letter-spacing: 10px; padding-left: 10px; }
  .label--front .brand { position: absolute; top: 130px; left: 0; right: 0; }
  .label--front .brand__name { font-size: 46px; }
  .label--front .brand__estate { font-size: 20px; margin-top: 10px; }
  .label--back .brand { position: absolute; top: 44px; left: 0; right: 0; }
  .label--back .brand__name { font-size: 34px; }
  .label--back .brand__estate { font-size: 14px; margin-top: 6px; }
  .varietal {
    position: absolute;
    left: 0;
    right: 0;
  }
  .varietal__region { font-size: 15px; letter-spacing: 2px; }
  .varietal__grape {
    font-family: "Pinyon Script", cursive;
    font-size: 30px;
    line-height: 1.15;
  }
  .varietal__place { font-size: 14px; letter-spacing: 3px; }
  .label--front .varietal { top: 412px; }
  .label--front .varietal__region { font-size: 17px; }
  .label--front .varietal__grape { font-size: 38px; }
  .label--front .varietal__place { font-size: 16px; letter-spacing: 4px; margin-top: 4px; }
  .vintage { font-size: 20px; letter-spacing: 3px; margin-top: 26px; }
  .label--back .varietal { top: 124px; }
  .back__rule {
    position: absolute;
    top: 252px;
    left: 50%;
    width: 110px;
    margin-left: -55px;
    border-top: 1.5px solid var(--ink);
  }
  .back__bottler {
    position: absolute;
    top: 280px;
    left: 0;
    right: 0;
    font-size: 13px;
    letter-spacing: 1px;
    line-height: 1.45;
  }
  .back__abv { font-size: 14px; letter-spacing: 1.5px; margin-top: 8px; }
  .back__warning {
    position: absolute;
    top: 380px;
    left: 44px;
    right: 44px;
    font-size: 12.5px;
    line-height: 1.5;
    letter-spacing: 0.8px;
    text-align: justify;
    text-transform: uppercase;
  }
  .back__warning strong { font-weight: 600; }
  .back__footer {
    position: absolute;
    left: 44px;
    right: 44px;
    bottom: 40px;
    display: flex;
    justify-content: space-between;
    font-size: 12.5px;
    letter-spacing: 1px;
  }
</style>
</head>
<body>
  <section class="label label--front" aria-label="Front label">
    <div class="label__frame"></div>
    <div class="seal"><div class="seal__ring">MARRICK</div></div>
    <h1 class="brand">
      <span class="brand__name">MARRICK</span>
      <span class="brand__estate">ESTATE</span>
    </h1>
    <div class="varietal">
      <p class="varietal__region">HOWELL MOUNTAIN</p>
      <p class="varietal__grape">Cabernet Sauvignon</p>
      <p class="varietal__place">NAPA VALLEY</p>
      <p class="vintage">2022</p>
    </div>
  </section>

  <section class="label label--back" aria-label="Back label">
    <div class="label__frame"></div>
    <h2 class="brand">
      <span class="brand__name">MARRICK</span>
      <span class="brand__estate">ESTATE</span>
    </h2>
    <div class="varietal">
      <p class="varietal__region">HOWELL MOUNTAIN</p>
      <p class="varietal__grape">Cabernet Sauvignon</p>
      <p class="varietal__place">NAPA VALLEY, 2022</p>
    </div>
    <div class="back__rule"></div>
    <div class="back__bottler">
      <p>CELLARED AND BOTTLED BY<br>MARRICK ESTATE, CALDER RIDGE, CA 95417</p>
      <p class="back__abv">ALC. 14.5% BY VOL.</p>
    </div>
    <p class="back__warning"><strong>Government Warning:</strong> (1) According to the Surgeon General, women should not drink alcoholic beverages during pregnancy because of the risk of birth defects. (2) Consumption of alcoholic beverages impairs your ability to drive a car or operate machinery, and may cause health problems.</p>
    <div class="back__footer">
      <span>750 ML</span>
      <span>CONTAINS SULFITES</span>
    </div>
  </section>
</body>
</html>
```